SaaS Early tech startup business card design

Unique design for experience ecommerce platform company. the business cards will be used by executive members. conformance with color code is required.

```html
<!DOCTYPE html>
<html lang="en">
<head>
<meta charset="utf-8">
<title>Velvik business card</title>
<link href="https://fonts.googleapis.com/css2?family=Arimo:wght@400;700&display=swap" rel="stylesheet">
<style>
  :root {
    --brand-blue: #1a668f;
    --brand-teal: #2bb89a;
    --paper: #ffffff;
    --backdrop: #c6c6c6;
    --rule: rgba(43, 184, 154, 0.55);
  }
  * { box-sizing: border-box; margin: 0; padding: 0; }
  html, body {
    width: 1200px; height: 788px; overflow: hidden;
    background: var(--backdrop);
    font-family: "Arimo", Arial, sans-serif;
  }
  .stage {
    position: relative; width: 1200px; height: 788px;
    display: flex; align-items: center; justify-content: center; gap: 40px;
  }
  .card {
    position: relative; width: 540px; height: 309px;
    border-radius: 18px; overflow: hidden;
    box-shadow: 0 10px 24px rgba(0,0,0,0.22);
  }
  .card-front { background: var(--paper); }
  .card-back {
    background: var(--brand-blue);
    display: flex; align-items: center; justify-content: center;
  }
  .front-shape { position: absolute; inset: 0; }
  .front-wordmark {
    position: absolute; left: 38px; bottom: 52px;
    font-weight: 700; font-size: 66px; letter-spacing: -1px;
    color: var(--brand-blue); line-height: 1;
  }
  .back-wordmark {
    font-weight: 700; font-size: 128px; letter-spacing: -2px;
    color: var(--paper); line-height: 1;
  }
  .contact-block {
    position: absolute; left: 300px; top: 42px; width: 220px;
    color: var(--paper);
  }
  .person-name {
    font-weight: 700; font-size: 19px; letter-spacing: 0.5px;
    color: var(--brand-teal); text-transform: uppercase;
  }
  .person-role { font-size: 13px; margin-top: 3px; }
  .divider { height: 1px; background: var(--rule); margin: 12px 0; width: 190px; }
  .address { font-size: 13px; line-height: 1.35; }
  .contact-list { list-style: none; font-size: 12.5px; line-height: 1.55; }
  .contact-list li { display: flex; align-items: center; gap: 7px; }
  .contact-list svg { width: 10px; height: 10px; flex: none; fill: var(--brand-teal); }
</style>
</head>
<body>
<main class="stage">
  <section class="card card-front" aria-label="Card front with contact details">
    <svg class="front-shape" viewBox="0 0 540 309" aria-hidden="true">
      <path d="M238 0 A290 290 0 0 0 372 309 H540 V0 Z" fill="var(--brand-blue)"/>
      <path d="M222 0 A296 296 0 0 0 352 296" fill="none" stroke="var(--brand-teal)" stroke-width="4"/>
    </svg>
    <div class="front-wordmark">velvik</div>
    <div class="contact-block">
      <h1 class="person-name">Dorian Hale</h1>
      <p class="person-role">Owner/CEO</p>
      <div class="divider"></div>
      <p class="address">210 - 4470 Harbor Ave<br>Lakeview, BC V2K4R7</p>
      <div class="divider"></div>
      <ul class="contact-list">
        <li><svg viewBox="0 0 10 10"><path d="M2 0.5 L4 2.5 L3 3.8 Q4.5 6 6.2 7 L7.5 6 L9.5 8 L8 9.5 Q3 9 0.5 2 Z"/></svg>(555) 014-7720</li>
        <li><svg viewBox="0 0 10 10"><path d="M0.5 3 Q5 0 9.5 3 L8 4.5 L7 3.5 H3 L2 4.5 Z M2 5 H8 V9.5 H2 Z"/></svg>(555) 019-3381 ext 114</li>
        <li><svg viewBox="0 0 10 10"><path d="M0.5 2 H9.5 V8.5 H0.5 Z M1.2 2.6 L5 5.6 L8.8 2.6" stroke="var(--brand-blue)" stroke-width="0.8"/></svg>dorian@northpinegroup.com</li>
        <li><svg viewBox="0 0 10 10"><circle cx="5" cy="5" r="4.5"/><path d="M0.5 5 H9.5 M5 0.5 Q2 5 5 9.5 M5 0.5 Q8 5 5 9.5" fill="none" stroke="var(--brand-blue)" stroke-width="0.7"/></svg>www.northpinegroup.com</li>
      </ul>
    </div>
  </section>
  <section class="card card-back" aria-label="Card back">
    <div class="back-wordmark">velvik</div>
  </section>
</main>
</body>
</html>
```